Providing Back Office Solutions to Financial Advisors and Attorney Needs a Business Card Design

Need a Business Card Design that speaks to Financial Advisor and Attorneys. Some of the word that come to mind is Clean/Simple & Futuristic.

Industry/Entity Type

Business

```html
<!DOCTYPE html>
<html lang="en">
<head>
<meta charset="utf-8">
<title>Alteris Back Office Solutions – Business Card</title>
<link rel="stylesheet" href="https://fonts.googleapis.com/css2?family=Montserrat:wght@500&family=Roboto+Condensed:wght@500&family=Merriweather+Sans:wght@500&family=Mulish:wght@400&display=swap">
<style>
  :root {
    --page-bg: #e8e5e1;
    --card-navy: #0f4a78;
    --card-blue: #1c6aa6;
    --card-deep: #12507f;
    --card-violet: #4b3f98;
    --ink-light: #eef2f6;
    --ink-soft: #c9d8e6;
    --ink-address: #d6c7c2;
  }
  * { margin: 0; padding: 0; box-sizing: border-box; }
  html, body {
    width: 1200px;
    height: 1054px;
    overflow: hidden;
    background: var(--page-bg);
  }
  .business-card {
    position: absolute;
    left: 100px;
    top: 224px;
    width: 1000px;
    height: 606px;
    overflow: hidden;
    background:
      radial-gradient(ellipse at 30% 45%, rgba(255,255,255,0.08), transparent 60%),
      linear-gradient(100deg, var(--card-navy) 0%, var(--card-blue) 45%, var(--card-deep) 75%);
    box-shadow: 0 18px 40px rgba(0,0,0,0.18);
  }
  .accent-band {
    position: absolute;
    top: 0;
    right: 0;
    width: 236px;
    height: 100%;
    background: linear-gradient(180deg, #3d4a9c 0%, var(--card-violet) 100%);
  }
  .brand-name {
    position: absolute;
    left: 48px;
    top: 50px;
    font-family: "Montserrat", sans-serif;
    font-weight: 500;
    font-size: 92px;
    letter-spacing: 6px;
    color: var(--ink-light);
    line-height: 1;
  }
  .brand-tagline {
    position: absolute;
    left: 52px;
    top: 164px;
    font-family: "Roboto Condensed", sans-serif;
    font-weight: 500;
    font-size: 35px;
    color: var(--ink-light);
    line-height: 1;
  }
  .person-name {
    position: absolute;
    left: 50px;
    top: 303px;
    font-family: "Merriweather Sans", sans-serif;
    font-weight: 500;
    font-size: 34px;
    color: var(--ink-light);
    line-height: 1;
  }
  .person-role {
    position: absolute;
    left: 50px;
    top: 355px;
    font-family: "Mulish", sans-serif;
    font-size: 23px;
    color: var(--ink-soft);
    line-height: 1;
  }
  .contact-list {
    position: absolute;
    left: 50px;
    top: 422px;
    list-style: none;
    font-family: "Mulish", sans-serif;
    font-size: 24px;
    color: var(--ink-light);
  }
  .contact-item {
    display: flex;
    align-items: center;
    height: 35.5px;
  }
  .contact-icon {
    width: 22px;
    height: 22px;
    margin-right: 26px;
    fill: var(--ink-soft);
  }
  .contact-address {
    position: absolute;
    left: 50px;
    top: 533px;
    font-family: "Mulish", sans-serif;
    font-size: 23px;
    color: var(--ink-address);
    line-height: 1;
  }
</style>
</head>
<body>
  <section class="business-card">
    <div class="accent-band"></div>

    <h1 class="brand-name">ALTERIS</h1>
    <p class="brand-tagline">BACK OFFICE SOLUTIONS</p>

    <h2 class="person-name">John Doe Smith</h2>
    <p class="person-role">Managing Director</p>

    <ul class="contact-list">
      <li class="contact-item">
        <svg class="contact-icon" viewBox="0 0 24 24" aria-hidden="true">
          <path d="M3 9c0-3 4-5 9-5s9 2 9 5v2h-5V8.5c-1-.5-2.5-.8-4-.8s-3 .3-4 .8V11H3z"/>
          <path d="M7 12h10l3 8H4z"/>
        </svg>
        <span>555.555.5555</span>
      </li>
      <li class="contact-item">
        <svg class="contact-icon" viewBox="0 0 24 24" aria-hidden="true">
          <path d="M2 5h20v14H2z M4 7v.5l8 6 8-6V7z M4 10v7h16v-7l-8 6z" fill-rule="evenodd"/>
        </svg>
        <span>johndoe@example.com</span>
      </li>
      <li class="contact-item">
        <svg class="contact-icon" viewBox="0 0 24 24" aria-hidden="true">
          <path d="M12 2a10 10 0 1 0 0 20 10 10 0 0 0 0-20zm0 2c1 1.3 1.8 3.2 2 5h-4c.2-1.8 1-3.7 2-5zm-2.4.4C8.8 6 8.2 7.5 8 9H4.6a8 8 0 0 1 5-4.6zm4.8 0A8 8 0 0 1 19.4 9H16c-.2-1.5-.8-3-1.6-4.6zM4.1 11H8v2H4.1a8 8 0 0 1 0-2zM10 11h4v2h-4zm6 0h3.9a8 8 0 0 1 0 2H16zM4.6 15H8c.2 1.5.8 3 1.6 4.6A8 8 0 0 1 4.6 15zm5.4 0h4c-.2 1.8-1 3.7-2 5-1-1.3-1.8-3.2-2-5zm6 0h3.4a8 8 0 0 1-5 4.6c.8-1.6 1.4-3.1 1.6-4.6z"/>
        </svg>
        <span>www.yourwebsite.com</span>
      </li>
    </ul>

    <p class="contact-address">234 Anywhere St., Any Town, US 123456</p>
  </section>
</body>
</html>
```